Sex trafficking Survivors Brochure ********

I need a general brochure for a new non-profit committed to empowering survivors of sexual exploitation. I kept the wording to a minimum so the design will help me tell the story. The brochure will be used in churches and other venues when I give presentations. I will also be using this in one on one presentations to walk through the highlights of our work. We are in the aftercare business and the feel should communicate hope and new beginnings.

I would like a single fold brochure- about 8.5x5.5.
Updates

to clarify- the brochure should be 8.5 by 5.5 Added Wednesday, November 05, 2014

Target Market(s)

donors, volunteers- all ages- mainly women

Industry/Entity Type

Non-Profit

Font styles to use
Serif

Requirements
Must have
• Pictures draw me in. I tend to like professional designs with just enough color and detail to make them unique.
• Hopeful- note the picture I attached are bright- not sad and depressed. Feel free to add your own photos if they are better. My favorite picture is the black woman with sun.
• Please use a variety of races- we serve a diverse population.
• I also need my website listed www.brightharborhome.org
Nice to have
• I have seen some designs that use one picture to stretch across the front and back of the brochure. This might be interesting if it works, but I may have too much text on the back to make this worthwhile.
Should not have
• hearts, country feel, goofy, whimsical

```html
<!DOCTYPE html>
<html lang="en">
<head>
<meta charset="utf-8">
<title>Bright Harbor Home – Brochure Inside Spread</title>
<link rel="stylesheet" href="https://fonts.googleapis.com/css2?family=Fondamento&family=Alegreya:ital,wght@0,400;0,700;1,400;1,700&family=Gentium+Book+Plus:wght@700&family=Marcellus&display=swap">
<style>
  :root {
    --gold: #f6b90a;
    --white: #ffffff;
    --teal-ink: #123f3f;
    --mission-blue: #1d6a9a;
    --mission-text: #2a79a8;
    --plum: #3b0f3f;
    --plum-text: #2c0f24;
    --cream: #f5ecd5;
  }
  html, body { margin: 0; padding: 0; overflow: hidden; }
  body { width: 1200px; height: 776px; background: #f1e6d0; }
  .spread { position: relative; width: 1200px; height: 776px; overflow: hidden; }
  .backdrop { position: absolute; inset: 0; }
  .txt { position: absolute; margin: 0; }

  .role-title {
    left: 115px; top: 18px; font-family: "Fondamento", serif;
    font-size: 84px; color: var(--gold); line-height: 1;
  }
  .role-head {
    font-family: "Fondamento", serif; font-size: 33px; color: var(--white);
    text-align: right; line-height: 1; text-shadow: 0 1px 3px rgba(0,0,0,.35);
  }
  .role-body {
    font-family: "Alegreya", serif; font-style: italic; font-size: 20px;
    line-height: 28px; color: var(--white); text-align: right;
    text-shadow: 0 1px 3px rgba(0,0,0,.4);
  }
  .vision-head {
    left: 708px; top: 12px; font-family: "Gentium Book Plus", serif;
    font-size: 30px; color: var(--teal-ink);
  }
  .vision-body {
    left: 655px; top: 50px; width: 150px; font-family: "Gentium Book Plus", serif;
    font-size: 17px; line-height: 23px; color: var(--teal-ink); text-align: center;
  }
  .mission-head {
    left: 845px; top: 22px; font-family: "Gentium Book Plus", serif;
    font-size: 46px; color: var(--mission-blue); line-height: 1;
  }
  .mission-body {
    left: 830px; top: 74px; width: 280px; font-family: "Gentium Book Plus", serif;
    font-size: 20px; line-height: 28px; color: var(--mission-text); text-align: center;
  }
  .model-head {
    left: 920px; top: 258px; font-family: "Marcellus", serif;
    font-size: 46px; color: var(--plum); line-height: 1;
  }
  .model-step {
    font-family: "Alegreya", serif; font-weight: 700; font-style: italic;
    font-size: 22px; color: var(--plum); line-height: 1;
  }
  .model-body {
    font-family: "Alegreya", serif; font-size: 18px; line-height: 23px; color: var(--plum-text);
  }
</style>
</head>
<body>
<main class="spread">
  <svg class="backdrop" width="1200" height="776" viewBox="0 0 1200 776">
    <defs>
      <linearGradient id="rightPhotoTone" x1="0" y1="0" x2="1" y2="1">
        <stop offset="0" stop-color="#fbe9cf"/>
        <stop offset=".45" stop-color="#efb36a"/>
        <stop offset=".8" stop-color="#d4782a"/>
        <stop offset="1" stop-color="#6a3a1c"/>
      </linearGradient>
      <linearGradient id="leftPhotoTone" x1="0" y1="0" x2="1" y2=".4">
        <stop offset="0" stop-color="#1e1a1a"/>
        <stop offset=".45" stop-color="#6b4a3b"/>
        <stop offset=".8" stop-color="#b5692b"/>
        <stop offset="1" stop-color="#d98a2c"/>
      </linearGradient>
      <linearGradient id="insetPhotoTone" x1="0" y1="0" x2="1" y2="1">
        <stop offset="0" stop-color="#5b8a4a"/>
        <stop offset=".5" stop-color="#4f6f7e"/>
        <stop offset="1" stop-color="#2a3550"/>
      </linearGradient>
      <linearGradient id="centerPhotoTone" x1="0" y1="0" x2=".3" y2="1">
        <stop offset="0" stop-color="#f3e4cf"/>
        <stop offset=".35" stop-color="#e2a58c"/>
        <stop offset=".7" stop-color="#b9533e"/>
        <stop offset="1" stop-color="#e0c2a4"/>
      </linearGradient>
      <radialGradient id="missionGlow" cx=".45" cy=".3" r=".7">
        <stop offset="0" stop-color="#ffffff"/>
        <stop offset=".7" stop-color="#fdf6ea"/>
        <stop offset="1" stop-color="#f8e3c4"/>
      </radialGradient>
    </defs>
    <rect width="1200" height="776" fill="url(#rightPhotoTone)" role="img" aria-label="Photo of a smiling woman in warm sunlight"/>
    <path d="M830 0 H1200 V110 C1150 215 1000 235 880 215 C820 200 815 100 830 0 Z" fill="url(#missionGlow)"/>
    <path d="M600 0 H845 C800 250 905 500 880 776 H540 C560 500 590 200 600 0 Z" fill="url(#centerPhotoTone)" role="img" aria-label="Photo of a laughing young woman making a peace sign"/>
    <path d="M640 0 H832 C805 100 795 190 822 250 C760 220 690 228 632 212 C642 140 642 60 640 0 Z" fill="var(--cream)"/>
    <path d="M0 0 H620 C590 200 560 500 540 776 H0 Z" fill="url(#leftPhotoTone)" role="img" aria-label="Photo of two smiling women talking together"/>
    <path d="M0 345 C120 300 265 390 300 776 H0 Z" fill="url(#insetPhotoTone)" role="img" aria-label="Photo of a smiling young woman holding books outdoors"/>
  </svg>

  <section class="your-role">
    <h1 class="txt role-title">Your Role</h1>
    <h2 class="txt role-head" style="right:632px; top:84px;">Mentor</h2>
    <p class="txt role-body" style="right:632px; top:122px; width:470px;">Build a safe nurturing relationship with one woman and encourage her to reach her goals.&nbsp; Join a community who receive training and support to effectively mentor.</p>
    <h2 class="txt role-head" style="right:632px; top:248px;">Teacher</h2>
    <p class="txt role-body" style="right:632px; top:286px; width:480px;">Teach group classes on life skills, biblical studies, physical wellbeing, creative arts, conflict resolution, emotional health, literacy, and financial management.</p>
    <h2 class="txt role-head" style="right:655px; top:410px;">Business Partner</h2>
    <p class="txt role-body" style="right:660px; top:448px; width:360px;">Provide employment and business coaching to a survivor.</p>
    <h2 class="txt role-head" style="right:695px; top:503px;">Supporter</h2>
    <p class="txt role-body" style="right:728px; top:540px; width:200px;">Financially and prayerfully support the work of Bright Harbor Home.</p>
  </section>

  <section class="vision">
    <h2 class="txt vision-head">Vision</h2>
    <p class="txt vision-body">Survivors of sexual exploitation live free, fulfilling their God-given purpose.</p>
  </section>

  <section class="mission">
    <h2 class="txt mission-head">Mission</h2>
    <p class="txt mission-body">Mobilize communities to encourage and equip survivors of sexual exploitation to build new lives.</p>
  </section>

  <section class="our-model">
    <h2 class="txt model-head">Our Model</h2>
    <h3 class="txt model-step" style="left:928px; top:314px;">Heal</h3>
    <p class="txt model-body" style="left:925px; top:338px; width:265px;">Survivors need safe relationships and a safe environment to heal.&nbsp; Bright Harbor Home facilitates mentor relationships, offers a supportive community and immerses survivors in faith-based curriculum.</p>
    <h3 class="txt model-step" style="left:913px; top:520px;">Discover</h3>
    <p class="txt model-body" style="left:910px; top:544px; width:285px;">In order to thrive, survivors need to discover their innate ability, preferences, personality and spiritual gifts.</p>
    <h3 class="txt model-step" style="left:893px; top:637px;">Overcome</h3>
    <p class="txt model-body" style="left:862px; top:661px; width:290px;">Survivors overcome barriers to moving ahead with the right educational and employment options.</p>
  </section>
</main>
</body>
</html>
```